Need a FLYER/BROCHURE for selling woman hair. I have an online business and need your help.

I need a flyer/BROCHURE that represents my company. We sale hair online and needing for our customers to know our prices and discounts for any holiday and upcoming new year specials. I need the brochure to stand out. Have our brand Logo on it. Pictures of hair we sale on our site and models on the flyer. Prices will need to be place on the flyer indicating before and after the discounts. I also have a bag gift for loyal customers that need to be on the flyer. Colors I am interested in are purple and Gold. Or something creative that will blend with my logo. On my prices I sent. I need to change the title Best, Medium and Low Quality to 6A, 5A, to The Orlena Selection.

Reason: I would like the deadline to change. The reason I see some designers are coming to my project and some are saying the deadline is too short. I would like to see what they can offer me before I decide.

Industry/Entity Type

Business

Requirements
Must have
• Pictures of my brand. Prices that matches my original prices and sales prices. Pictures of hair and models.

```html
<!DOCTYPE html>
<html lang="en">
<head>
<meta charset="utf-8">
<title>Orlena Natural Hair – Offer Prices Flyer</title>
<link rel="stylesheet" href="https://fonts.googleapis.com/css2?family=Baloo+2:wght@600;800&family=Marcellus&family=Open+Sans:wght@400;600&display=swap">
<style>
  :root{
    --purple:#2e0f4a;
    --purple-deep:#1f0834;
    --gold:#d8b45a;
    --gold-light:#efe0a8;
    --paper:#ffffff;
    --stage:#1c1c1e;
    --ink:#111111;
  }
  *{box-sizing:border-box;margin:0;padding:0}
  html,body{width:1200px;height:1200px;overflow:hidden;background:var(--stage)}
  .flyer{
    position:absolute;left:170px;top:20px;width:860px;height:1160px;
    background:var(--paper);overflow:hidden;
    font-family:"Baloo 2",sans-serif;
  }
  /* header */
  .header-band{
    position:absolute;left:0;top:0;width:100%;height:150px;
    background:linear-gradient(135deg,var(--purple-deep),var(--purple) 60%,var(--purple-deep));
    border-bottom:6px solid var(--gold);
  }
  .header-band::after{
    content:"";position:absolute;left:0;right:0;bottom:-16px;height:4px;background:var(--gold-light);
  }
  .title{
    position:absolute;right:60px;top:40px;
    font-family:"Marcellus",serif;font-size:72px;color:var(--gold);letter-spacing:1px;
  }
  .brand-circle{
    position:absolute;left:-30px;top:-40px;width:330px;height:330px;border-radius:50%;
    background:radial-gradient(circle at 50% 40%,var(--purple),var(--purple-deep));
    border:8px solid var(--gold);
    display:flex;flex-direction:column;align-items:center;justify-content:center;padding-top:40px;
  }
  .brand-name{
    font-family:"Marcellus",serif;color:var(--gold);font-size:34px;line-height:1.05;text-align:center;text-transform:uppercase;
  }
  /* price tables */
  .price-grid{
    position:absolute;left:34px;top:190px;display:flex;gap:22px;
  }
  .column{width:180px;display:flex;flex-direction:column;gap:26px}
  .column.c1{margin-top:120px}
  .column.c2{margin-top:50px}
  .column.c3{margin-top:20px}
  .column.c4{margin-top:0}
  .table-title{
    background:var(--purple);color:var(--gold);text-transform:uppercase;
    font-weight:800;font-size:19px;line-height:1;padding:7px 14px 5px;
    clip-path:polygon(10px 0,100% 0,calc(100% - 10px) 100%,0 100%);
    margin-bottom:4px;
  }
  .table-title small{display:block;font-size:10px;font-weight:600;letter-spacing:.3px;margin-top:1px}
  .row{
    display:grid;grid-template-columns:1fr 1fr;height:22px;margin-bottom:3px;
    font-size:19px;font-weight:800;line-height:24px;color:var(--gold);text-align:center;
  }
  .row.body{background:var(--purple);clip-path:polygon(8px 0,100% 0,calc(100% - 8px) 100%,0 100%)}
  .row span+span{border-left:2px solid var(--gold)}
  .row.head{font-size:18px}
  /* bottom */
  .model-strip{
    position:absolute;left:0;top:960px;width:100%;height:130px;
    background:linear-gradient(90deg,#c9a88a,#6b4a35 30%,#e4c2a6 50%,#3a2620 70%,#d9b48e);
    border-top:5px solid var(--gold);
  }
  .slogan-band{
    position:absolute;left:0;top:1060px;width:100%;height:50px;
    background:linear-gradient(90deg,var(--gold-light),var(--gold),var(--gold-light));
    display:flex;align-items:center;justify-content:center;
  }
  .slogan{font-size:40px;font-weight:800;color:var(--ink);line-height:1;padding-top:6px}
  .footer{
    position:absolute;left:0;top:1110px;width:100%;height:50px;background:var(--purple);
    display:flex;align-items:center;justify-content:center;gap:16px;
    font-family:"Open Sans",sans-serif;color:var(--gold);font-size:20px;
  }
  .footer .web{color:#fff;font-weight:600}
</style>
</head>
<body>
<div class="flyer">
  <div class="header-band"><div class="title">Offer Prices ...!</div></div>
  <div class="brand-circle"><div class="brand-name">Orlena<br>Natural Hair</div></div>

  <div class="price-grid">
    <div class="column c1">
      <div class="price-table">
        <div class="table-title">High Quality</div>
        <div class="row head"><span>INCH</span><span>60%</span></div>
        <div class="row body"><span>12</span><span>55</span></div>
        <div class="row body"><span>14</span><span>62</span></div>
        <div class="row body"><span>16</span><span>74</span></div>
        <div class="row body"><span>18</span><span>81</span></div>
        <div class="row body"><span>20</span><span>88</span></div>
        <div class="row body"><span>22</span><span>97</span></div>
        <div class="row body"><span>24</span><span>107</span></div>
        <div class="row body"><span>26</span><span>112</span></div>
        <div class="row body"><span>28</span><span>120</span></div>
        <div class="row body"><span>30</span><span>128</span></div>
      </div>
      <div class="price-table">
        <div class="table-title">Cheap Lace Closure</div>
        <div class="row head"><span>INCH</span><span>60%</span></div>
        <div class="row body"><span>10</span><span>43</span></div>
        <div class="row body"><span>12</span><span>48</span></div>
        <div class="row body"><span>14</span><span>53</span></div>
        <div class="row body"><span>16</span><span>58</span></div>
        <div class="row body"><span>18</span><span>62</span></div>
        <div class="row body"><span>20</span><span>66</span></div>
      </div>
    </div>

    <div class="column c2">
      <div class="price-table">
        <div class="table-title">Medium Quality</div>
        <div class="row head"><span>INCH</span><span>60%</span></div>
        <div class="row body"><span>12</span><span>43</span></div>
        <div class="row body"><span>14</span><span>48</span></div>
        <div class="row body"><span>16</span><span>53</span></div>
        <div class="row body"><span>18</span><span>59</span></div>
        <div class="row body"><span>20</span><span>64</span></div>
        <div class="row body"><span>22</span><span>69</span></div>
        <div class="row body"><span>24</span><span>80</span></div>
        <div class="row body"><span>26</span><span>85</span></div>
        <div class="row body"><span>28</span><span>91</span></div>
        <div class="row body"><span>30</span><span>96</span></div>
        <div class="row body"><span>32</span><span>98</span></div>
        <div class="row body"><span>34</span><span>99</span></div>
        <div class="row body"><span>36</span><span>104</span></div>
        <div class="row body"><span>38</span><span>107</span></div>
        <div class="row body"><span>40</span><span>114</span></div>
      </div>
      <div class="price-table">
        <div class="table-title">Best Lace Frontal<small>13X4</small></div>
        <div class="row head"><span>INCH</span><span>60%</span></div>
        <div class="row body"><span>12</span><span>172</span></div>
        <div class="row body"><span>14</span><span>177</span></div>
        <div class="row body"><span>16</span><span>186</span></div>
        <div class="row body"><span>18</span><span>203</span></div>
      </div>
    </div>

    <div class="column c3">
      <div class="price-table">
        <div class="table-title">Low Quality</div>
        <div class="row head"><span>INCH</span><span>60%</span></div>
        <div class="row body"><span>12</span><span>29</span></div>
        <div class="row body"><span>14</span><span>33</span></div>
        <div class="row body"><span>16</span><span>39</span></div>
        <div class="row body"><span>18</span><span>42</span></div>
        <div class="row body"><span>20</span><span>46</span></div>
        <div class="row body"><span>22</span><span>50</span></div>
        <div class="row body"><span>24</span><span>54</span></div>
        <div class="row body"><span>26</span><span>59</span></div>
        <div class="row body"><span>28</span><span>65</span></div>
        <div class="row body"><span>30</span><span>81</span></div>
      </div>
      <div class="price-table">
        <div class="table-title">Cheap Lace Frontal<small>13X4</small></div>
        <div class="row head"><span>INCH</span><span>60%</span></div>
        <div class="row body"><span>12</span><span>120</span></div>
        <div class="row body"><span>14</span><span>126</span></div>
        <div class="row body"><span>16</span><span>134</span></div>
        <div class="row body"><span>18</span><span>142</span></div>
      </div>
      <div class="price-table">
        <div class="table-title">Deep Wave</div>
        <div class="row head"><span>INCH</span><span>60%</span></div>
        <div class="row body"><span>18</span><span>66</span></div>
        <div class="row body"><span>20</span><span>75</span></div>
        <div class="row body"><span>22</span><span>86</span></div>
        <div class="row body"><span>24</span><span>94</span></div>
      </div>
    </div>

    <div class="column c4">
      <div class="price-table">
        <div class="table-title">Bes Lace Closure</div>
        <div class="row head"><span>INCH</span><span>60%</span></div>
        <div class="row body"><span>12</span><span>64</span></div>
        <div class="row body"><span>14</span><span>70</span></div>
        <div class="row body"><span>16</span><span>78</span></div>
        <div class="row body"><span>18</span><span>86</span></div>
        <div class="row body"><span>20</span><span>92</span></div>
        <div class="row body"><span>22</span><span>102</span></div>
        <div class="row body"><span>24</span><span>104</span></div>
      </div>
      <div class="price-table">
        <div class="table-title">Solid Color Hair<small>Straight and Body Wave</small></div>
        <div class="row head"><span>INCH</span><span>60%</span></div>
        <div class="row body"><span>18</span><span>63</span></div>
        <div class="row body"><span>20</span><span>72</span></div>
        <div class="row body"><span>22</span><span>83</span></div>
        <div class="row body"><span>24</span><span>90</span></div>
      </div>
      <div class="price-table">
        <div class="table-title">Ombre Hair<small>Straight and Body Wave</small></div>
        <div class="row head"><span>INCH</span><span>60%</span></div>
        <div class="row body"><span>12</span><span>50</span></div>
        <div class="row body"><span>14</span><span>56</span></div>
        <div class="row body"><span>16</span><span>67</span></div>
        <div class="row body"><span>18</span><span>74</span></div>
        <div class="row body"><span>20</span><span>80</span></div>
        <div class="row body"><span>22</span><span>88</span></div>
        <div class="row body"><span>24</span><span>98</span></div>
      </div>
    </div>
  </div>

  <div class="model-strip" role="img" aria-label="Row of models showing long, curly and colored hair styles"></div>
  <div class="slogan-band"><div class="slogan">Long, Short, Colored...We love it!</div></div>
  <div class="footer"><span>Phone number and address data</span><span>|</span><span class="web">Orlenanatural.com</span></div>
</div>
</body>
</html>
```